OLVAK Web Design (Need help to re-design our website)

We need someone to help us re-design our website and launch it. All contents for the website are ready. (https://olvak.example.au/)

-Rearrange categories:
1. Heating & Cooling
2. Remove Home Appliance
3. Remove Entertainment

Home page - redesign (It will be a nice touch if the banner is in the loop).

NOTE:
-Brand colour blue and orange.
-Try using professional fonts (Example: Helvetica, etc.)
-The website's Footer should be readable and use light colour.

Target Market(s)

Residentials & commercial buildings

Industry/Entity Type

Heat Ventilation and Cooling Industry, Technology , Renewables

Coding

Coded - Design and coding required

Colors
0094D4
00A9DD
6FCCEA
C7EBF8
E9F6FB
59FF00
82FF00
B8FF75
E3FFCB
F4FFEA
F0912C
F2A743
F7CA91
FBE8D2
FDF5EE

Requirements
Nice to have
• Effects/transition on the words/copy/images.

```html
<!DOCTYPE html>
<html lang="en">
<head>
<meta charset="utf-8">
<title>OLVAK – Heating &amp; Cooling</title>
<link href="https://fonts.googleapis.com/css2?family=Poppins:wght@400;500;600;700&family=Josefin+Sans:wght@300;400&display=swap" rel="stylesheet">
<style>
:root{
  --blue:#0094D4;
  --blue-mid:#00A9DD;
  --blue-soft:#6FCCEA;
  --blue-pale:#C7EBF8;
  --blue-ice:#E9F6FB;
  --orange:#F0912C;
  --orange-soft:#F2A743;
  --ink:#1e1e1e;
  --text:#555;
  --white:#fff;
}
*{margin:0;padding:0;box-sizing:border-box}
html,body{width:1200px;height:3598px;overflow:hidden}
body{position:relative;font-family:'Josefin Sans',sans-serif;color:var(--ink);background:var(--white)}
.abs{position:absolute}
.btn{position:absolute;display:flex;align-items:center;justify-content:center;background:var(--orange);color:var(--white);font-family:'Poppins',sans-serif;font-size:17px;text-transform:uppercase}
.bubble{position:absolute;border-radius:50%;background:linear-gradient(135deg,var(--blue-soft),var(--blue))}
.photo{position:absolute;border-radius:50%;overflow:hidden}

/* hero */
.hero{position:absolute;left:0;top:0;width:1200px;height:687px;background:linear-gradient(120deg,#cfe9f2 0%,#b9dfee 45%,#c3e5f1 100%)}
.topbar-note{left:42px;top:12px;font-family:'Poppins',sans-serif;font-size:15px}
.topbar-note span{color:var(--blue)}
.topbar-contact{top:16px;font-family:'Poppins',sans-serif;font-size:11px;color:#666;display:flex;align-items:center;gap:6px}
.topbar-contact i{display:inline-block;width:9px;height:6px;background:var(--orange);border-radius:1px}
.brand{display:flex;align-items:center;gap:12px;font-family:'Poppins',sans-serif;font-weight:700;color:var(--blue-mid);letter-spacing:5px}
.brand i{display:block;border-radius:50%;background:var(--orange)}
.nav{left:298px;top:67px;display:flex;gap:32px;font-family:'Poppins',sans-serif;font-size:15px;font-weight:500}
.hero-tag{left:34px;top:242px;width:243px;height:42px;background:var(--orange);color:var(--white);font-family:'Poppins',sans-serif;font-weight:600;font-size:33px;line-height:42px;padding-left:9px}
.hero-title{left:36px;top:295px;font-family:'Poppins',sans-serif;font-weight:700;font-size:56px;color:#2b2b2b;letter-spacing:1px}
.hero-sub{left:42px;top:366px;font-family:'Poppins',sans-serif;font-weight:600;font-size:33px;color:#555}
.compliant{left:43px;top:555px;font-family:'Poppins',sans-serif;font-weight:600;font-size:15px;line-height:19px}
.badge{position:absolute;top:537px;width:76px;height:76px;border-radius:50%}

/* solutions */
.solutions{position:absolute;left:0;top:687px;width:1200px;height:752px;background:var(--blue-pale)}
.sec-title{font-family:'Poppins',sans-serif;font-weight:600;font-size:33px;text-align:center;width:1200px;left:0}
.sec-sub{width:1200px;left:0;text-align:center;font-size:19px;color:#333;font-weight:300}
.card{position:absolute;top:922px;width:288px;height:398px;background:var(--blue-ice)}
.card .img{height:205px}
.card h3{font-family:'Poppins',sans-serif;font-weight:600;font-size:22px;text-align:center;margin-top:52px}
.card .btn{left:46px;top:324px;width:196px;height:50px}

/* story */
.story-title{font-family:'Poppins',sans-serif;font-weight:600;font-size:32px}
.story-text{left:590px;top:1720px;width:536px;font-size:19px;line-height:27.5px;color:var(--text);font-weight:300}

/* hvac list */
.hvac-list{left:122px;top:2335px;list-style:none;font-family:'Poppins',sans-serif;font-weight:500;font-size:20px}
.hvac-list li{display:flex;align-items:center;height:52px}
.hvac-list li::before{content:"";width:40px;height:10px;background:var(--orange);border-radius:6px 1px 6px 1px;margin-right:22px}

/* question */
.question{position:absolute;left:0;top:2755px;width:1200px;height:318px;background:linear-gradient(110deg,#d3ebf4,#b9dfee 60%,#cbe7f2)}
.call{font-family:'Poppins',sans-serif;font-weight:600;font-size:40px;color:var(--orange);text-align:center;width:1200px;left:0}

/* footer */
.footer{position:absolute;left:0;top:3080px;width:1200px;height:518px;background:var(--blue-pale)}
.foot-h{font-family:'Poppins',sans-serif;font-weight:600;font-size:20px;color:var(--blue)}
.foot-list{list-style:none;font-size:19px;color:#333;line-height:26px;font-weight:300}
.foot-list li{margin-bottom:20px}
.foot-text{font-size:19px;line-height:27px;color:#555;font-weight:300}
.social{position:absolute;top:3420px;width:26px;height:26px;border-radius:50%;border:3px solid var(--orange)}
.email-field{left:926px;top:3339px;width:222px;height:43px;background:var(--white);font-size:18px;color:#888;padding:14px 0 0 22px;font-weight:300}
</style>
</head>
<body>

<section class="hero" aria-label="Hero">
  <div class="abs" role="img" aria-label="Soft-focus living room with family relaxing on a sofa" style="left:0;top:0;width:1200px;height:687px;background:linear-gradient(120deg,rgba(255,255,255,.15),rgba(120,180,200,.18))"></div>
</section>

<p class="abs topbar-note">Don't miss our <span>Latest Promotions</span></p>
<p class="abs topbar-contact" style="left:880px"><i></i>hello@olvak.example.au</p>
<p class="abs topbar-contact" style="left:1032px"><i style="width:7px;height:7px;border-radius:50%"></i>(123) 456 7890</p>

<div class="abs brand" style="left:42px;top:54px;font-size:34px"><i style="width:30px;height:30px"></i>OLVAK</div>
<nav class="abs nav"><span>HOME</span><span>HEATING &amp; COOLING</span><span>OUR STORY</span><span>SUPPORT</span><span>BOOK APPOINTMENT</span></nav>
<div class="btn" style="left:993px;top:59px;width:144px;height:37px;font-size:16px">STAFF LOGIN</div>

<div class="abs hero-tag">Revolutionise</div>
<h1 class="abs hero-title">HEATING &amp; COOLING</h1>
<p class="abs hero-sub">Industry Australiawide</p>
<div class="btn" style="left:45px;top:437px;width:142px;height:37px;font-size:16px">BOOK NOW</div>
<p class="abs compliant">FULLY COMPLIANT WITH<br>ALL GOVERNMENT REBATES</p>
<div class="badge" style="left:299px;background:#8aa3c9"></div>
<div class="badge" style="left:413px;background:#c8a43a"></div>
<div class="badge" style="left:522px;background:var(--white)"></div>

<div class="bubble" style="left:771px;top:222px;width:386px;height:386px;background:var(--blue-mid)"></div>
<div class="bubble" style="left:804px;top:137px;width:66px;height:66px"></div>
<div class="bubble" style="left:741px;top:262px;width:32px;height:32px"></div>
<div class="abs" role="img" aria-label="Heat pump water tank and outdoor heat pump unit" style="left:808px;top:218px;width:350px;height:424px;background:linear-gradient(135deg,#f2f3f4,#d9dde0)"></div>

<section class="solutions" aria-label="Solutions"></section>
<h2 class="abs sec-title" style="top:778px">OFFERING SOLUTIONS FOR</h2>
<p class="abs sec-sub" style="top:838px">Please select from a category below that best suits your requirements.</p>

<article class="card" style="left:123px">
  <div class="img" role="img" aria-label="Modern home interior with appliances" style="background:linear-gradient(135deg,#8a8a8a,#3b3b3b)"></div>
  <h3>Residential</h3><div class="btn">READ MORE</div>
</article>
<article class="card" style="left:462px">
  <div class="img" role="img" aria-label="Technician servicing pipework" style="background:linear-gradient(135deg,#3e5d91,#d6dbe2)"></div>
  <h3>Trade</h3><div class="btn">READ MORE</div>
</article>
<article class="card" style="left:800px">
  <div class="img" role="img" aria-label="Commercial office building at dusk" style="background:linear-gradient(180deg,#8f95c4,#6a6450 70%,#3a3a3a)"></div>
  <h3>Commercial</h3><div class="btn">READ MORE</div>
</article>

<div class="bubble" style="left:349px;top:1540px;width:184px;height:184px"></div>
<div class="photo" role="img" aria-label="Installers fitting ceiling ductwork" style="left:68px;top:1558px;width:390px;height:390px;background:linear-gradient(135deg,#c9c9c9,#4a6fa8 60%,#2b2b2b)"></div>
<div class="photo" role="img" aria-label="Outdoor heat pump unit on grass" style="left:293px;top:1746px;width:244px;height:244px;background:linear-gradient(180deg,#dfe3e6,#f5f5f5 60%,#7a9a55);border:4px solid var(--white)"></div>
<div class="bubble" style="left:158px;top:1943px;width:92px;height:92px"></div>
<div class="bubble" style="left:258px;top:2023px;width:56px;height:56px"></div>
<h2 class="abs story-title" style="left:590px;top:1638px">OUR STORY</h2>
<p class="abs story-text">OLVAK is a company dedicated to manufacturing and installing energy-efficient products that reduce energy consumption, save costs, and promote sustainability. Our mission is to help individuals and businesses reduce their carbon footprint while also enhancing their comfort and quality of life.</p>
<div class="btn" style="left:590px;top:1897px;width:196px;height:49px">READ MORE</div>

<h2 class="abs story-title" style="left:122px;top:2250px">HEATING AND COOLING</h2>
<ul class="abs hvac-list">
  <li>HEAT PUMPS</li><li>AIR CONDITIONERS</li><li>SWIMMING POOL HEAT PUMP</li><li>MONOBLOCK HEAT PUMP</li>
</ul>
<div class="btn" style="left:120px;top:2551px;width:196px;height:49px">GET A QUOTE</div>
<div class="bubble" style="left:952px;top:2137px;width:188px;height:188px"></div>
<div class="photo" role="img" aria-label="Heat pump water tank against a brick wall" style="left:675px;top:2157px;width:388px;height:388px;background:linear-gradient(135deg,#a89684,#6e5e50 60%,#7c8e4c)"></div>
<div class="photo" role="img" aria-label="Technician servicing an outdoor unit" style="left:894px;top:2343px;width:246px;height:246px;background:linear-gradient(135deg,#6b8a3e,#d9c7a8 50%,#e8ecef);border:4px solid var(--white)"></div>
<div class="bubble" style="left:765px;top:2542px;width:90px;height:90px"></div>
<div class="bubble" style="left:865px;top:2642px;width:56px;height:56px"></div>

<section class="question" aria-label="Contact call-out"></section>
<h2 class="abs sec-title" style="top:2862px;font-size:50px;font-weight:700">HAVE A QUESTION?</h2>
<p class="abs call" style="top:2932px">Call : 1800 555 010</p>

<footer class="footer" aria-label="Footer"></footer>
<div class="abs brand" style="left:73px;top:3188px;font-size:34px"><i style="width:30px;height:30px"></i>OLVAK</div>
<p class="abs foot-text" style="left:75px;top:3256px;width:290px">OLVAK is a company dedicated to manufacturing and installing energy-efficient products that reduce energy consumption, save costs, and promote sustainability.</p>
<span class="social" style="left:70px"></span>
<span class="social" style="left:139px"></span>
<span class="social" style="left:211px"></span>

<h3 class="abs foot-h" style="left:437px;top:3188px">OUR PRODUCTS</h3>
<ul class="abs foot-list" style="left:437px;top:3245px;width:210px">
  <li>Heatpump</li><li>Air Conditioners</li><li>Swimming Pool Heat Pumps</li><li>Monoblock Heat Pumps</li>
</ul>
<h3 class="abs foot-h" style="left:696px;top:3188px">USEFUL LINKS</h3>
<ul class="abs foot-list" style="left:696px;top:3245px">
  <li>Our Story</li><li>Support</li><li>Promotions</li><li>Appointment</li>
</ul>
<h3 class="abs foot-h" style="left:926px;top:3188px">STAY CONNECTED</h3>
<p class="abs foot-text" style="left:926px;top:3242px;width:240px">Enter your email address to register to our newsletter subscription</p>
<div class="abs email-field">Email Address</div>
<div class="btn" style="left:926px;top:3390px;width:222px;height:43px;font-size:19px;font-weight:600">SUBSCRIBE NOW</div>

<p class="abs foot-text" style="left:71px;top:3543px">Copyright 2024 , All Rights Reserved</p>
<p class="abs foot-text" style="left:849px;top:3543px">Privacy Policy | Terms &amp; Conditions</p>

</body>
</html>
```